Brevin Finance Flyer Design

I would like a high res flyer designed for mass printing. It is for a mortgage and finance broking company in Sydney. We are called Brevin Finance. The wording i would like displayed is the following
Looking For Something Extra from your broker?
Brevin Finance can make all the difference
What we offer you is an extensive range of mortgage and finance products, including:
• Home Loans
• Investment Loans
• Low Doc Loans
• Vehicle Finance
• Equipment Finance
• Commercial Loans
• Refinance
Contact Us
Phone (02) 7354 2816
email info@brevinfinance.com.au
web www.brevinfinance.com.au
Finance

```html
<!DOCTYPE html>
<html lang="en">
<head>
<meta charset="utf-8">
<title>Brevin Finance Flyer</title>
<link rel="stylesheet" href="https://fonts.googleapis.com/css2?family=Lato:wght@300;400;700&family=Arimo:wght@700&display=swap">
<style>
  :root {
    --page-bg: #e9e7e3;
    --paper: #ffffff;
    --ink: #2b3340;
    --ink-soft: #4a4f57;
    --accent: #1e95cf;
    --navy: #1b3158;
    --photo-light: #dde7f2;
    --photo-mid: #b4c6dc;
    --photo-deep: #6f86aa;
  }
  * { box-sizing: border-box; margin: 0; padding: 0; }
  html, body {
    width: 918px; height: 1200px; overflow: hidden;
    background: var(--page-bg);
  }
  .flyer {
    position: absolute; left: 34px; top: 0;
    width: 658px; height: 930px;
    transform: scale(1.2903); transform-origin: 0 0;
    background: var(--paper);
    overflow: hidden;
    font-family: "Lato", sans-serif;
    color: var(--ink);
  }
  .hero-photo {
    position: absolute; left: 0; right: 0; top: 340px; bottom: 0;
    background:
      linear-gradient(to bottom, rgba(255,255,255,1) 0%, rgba(255,255,255,0) 35%),
      linear-gradient(100deg, var(--photo-light) 0%, var(--photo-light) 40%, var(--photo-mid) 70%, var(--photo-deep) 100%);
  }
  .brand { position: absolute; left: 45px; top: 58px; display: flex; align-items: center; gap: 14px; }
  .brand-mark { width: 40px; height: 40px; background: var(--ink-soft); }
  .brand-name { font-size: 44px; font-weight: 400; color: var(--ink-soft); line-height: 1; letter-spacing: -0.5px; }
  .brand-tagline { position: absolute; left: 108px; top: 104px; font-size: 15px; color: var(--ink-soft); }
  .headline {
    position: absolute; left: 110px; top: 152px;
    font-size: 39px; font-weight: 400; line-height: 35px;
    text-transform: uppercase; color: var(--navy); letter-spacing: -0.3px;
  }
  .subhead {
    position: absolute; left: 110px; top: 268px;
    font-size: 19px; font-weight: 400; color: var(--accent); text-transform: uppercase;
  }
  .intro {
    position: absolute; left: 111px; top: 296px; width: 450px;
    font-size: 17px; line-height: 22px; color: var(--ink-soft);
  }
  .product-list {
    position: absolute; left: 114px; top: 352px;
    list-style: none; font-size: 17.5px; line-height: 26.8px; color: var(--ink-soft);
  }
  .product-list li::before { content: "•"; color: var(--accent); margin-right: 6px; }
  .contact-title {
    position: absolute; left: 118px; top: 788px;
    font-family: "Arimo", sans-serif; font-weight: 700; font-size: 19px; color: var(--navy);
  }
  .contact-box {
    position: absolute; left: 120px; top: 816px; width: 285px; height: 114px;
    background: var(--navy);
  }
  .contact-line {
    position: absolute; left: 126px;
    font-family: "Arimo", sans-serif; font-weight: 700; font-size: 19px; color: #ffffff;
  }
  .contact-icon { position: absolute; left: 87px; width: 18px; height: 18px; }
</style>
</head>
<body>
  <main class="flyer">
    <div class="hero-photo" role="img" aria-label="Photo of business people walking through a bright office corridor"></div>

    <div class="brand">
      <span class="brand-mark"></span>
      <span class="brand-name">Brevin Finance</span>
    </div>
    <p class="brand-tagline">mortgage and finance broking services</p>

    <h1 class="headline">Looking for<br>something extra<br>from your broker?</h1>
    <h2 class="subhead">Brevin Finance can make all the difference.</h2>
    <p class="intro">What we offer you is an extensive range of mortgage and finance products, including:</p>
    <ul class="product-list">
      <li>Home Loans</li>
      <li>Investment Loans</li>
      <li>Low Doc Loans</li>
      <li>Vehicle Finance</li>
      <li>Equipment Finance</li>
      <li>Commercial Loans</li>
      <li>Refinance</li>
    </ul>

    <h3 class="contact-title">CONTACT US</h3>
    <div class="contact-box"></div>

    <svg class="contact-icon" style="top:829px" viewBox="0 0 18 18" aria-hidden="true">
      <rect width="18" height="18" rx="3" fill="#1b3158"/>
      <path d="M6 4 h2 l0.5 3 -1.5 1 q1 2.5 3 3.5 l1-1.5 3 0.5 v2 q-1 1.5 -3 1 q-5 -2 -6.5 -7 q-0.3 -2 1.5 -2.5z" fill="#fff"/>
    </svg>
    <span class="contact-line" style="top:827px">(02) 7354 2816</span>

    <svg class="contact-icon" style="top:862px" viewBox="0 0 18 18" aria-hidden="true">
      <rect width="18" height="18" rx="3" fill="#1b3158"/>
      <rect x="3.5" y="5" width="11" height="8" fill="#fff"/>
      <path d="M3.5 5 L9 9.5 L14.5 5" fill="none" stroke="#1b3158" stroke-width="1.2"/>
    </svg>
    <span class="contact-line" style="top:859px">info@brevinfinance.com.au</span>

    <svg class="contact-icon" style="top:895px" viewBox="0 0 18 18" aria-hidden="true">
      <rect width="18" height="18" rx="3" fill="#1b3158"/>
      <circle cx="9" cy="9" r="5" fill="none" stroke="#fff" stroke-width="1.3"/>
      <ellipse cx="9" cy="9" rx="2.2" ry="5" fill="none" stroke="#fff" stroke-width="1"/>
      <line x1="4" y1="9" x2="14" y2="9" stroke="#fff" stroke-width="1"/>
    </svg>
    <span class="contact-line" style="top:891px">www.brevinfinance.com.au</span>
  </main>
</body>
</html>
```